Business Card Design Project

We need a business card design template for a direct sales company that is branded to the company but the name information can be changed for the representatives. The card needs to include the company logo and website...www.gokelvara.example. It should also include the Customer Service number which is 1-800-482-Kelvra.

The front should have a space with the name and a place for their phone contact information and email address.
Updates

The card should be two sided.  It could also include the tagline "Kelvra is all about K!" or any of the information from www.gokelvara.example.

I am uploading the other formats that I currently have for the logo.

Thank you

Target Market(s)

The representatives are teenage girls that are 13-19 but they are selling products to all ages.

Industry/Entity Type

Business

Requirements
Must have
• A field with the toll free customer service number.
The company logo.
The company website information.
The company representative name.
The company representative phone number.
The company representative email contact info.
Nice to have
• QR Code which we already have.
Should not have
• Do not make it look like a design for children. It should be modern and professional but sophisticated.

```html
<!DOCTYPE html>
<html lang="en">
<head>
<meta charset="utf-8">
<title>Kelvra Representative Business Card</title>
<link rel="stylesheet" href="https://fonts.googleapis.com/css2?family=Cabin:wght@500;600;700&family=Oswald:wght@400;500&display=swap">
<style>
  :root {
    --card-bg: #e6e8e8;
    --card-glow: #fafafa;
    --ink-dark: #333638;
    --ink-light: #ffffff;
    --brand-pink: #e81bd6;
    --wave-pink: #f21ee3;
    --wave-soft: #f08ae6;
    --wave-fade: #e6b6e2;
  }
  * { margin: 0; padding: 0; box-sizing: border-box; }
  html, body {
    width: 1200px;
    height: 700px;
    overflow: hidden;
    background: var(--card-bg);
  }
  .business-card {
    position: relative;
    width: 1200px;
    height: 700px;
    overflow: hidden;
    background:
      radial-gradient(ellipse 520px 320px at 300px 140px, var(--card-glow) 0%, rgba(250,250,250,0) 100%),
      linear-gradient(180deg, #eef0f0 0%, var(--card-bg) 100%);
    font-family: "Cabin", "Gill Sans", sans-serif;
  }
  .card-shapes {
    position: absolute;
    inset: 0;
    width: 1200px;
    height: 700px;
  }
  .brand-block {
    position: absolute;
    left: 50px;
    top: 70px;
    display: flex;
    flex-direction: column;
    align-items: flex-end;
  }
  .brand-name {
    display: flex;
    align-items: center;
    gap: 18px;
    font-family: "Cabin", "Gill Sans", sans-serif;
    font-weight: 600;
    font-size: 100px;
    line-height: 1;
    letter-spacing: 2px;
    color: var(--ink-dark);
  }
  .brand-dot {
    width: 46px;
    height: 46px;
    border-radius: 50%;
    background: var(--brand-pink);
  }
  .brand-website {
    margin-top: 6px;
    font-family: "Cabin", "Gill Sans", sans-serif;
    font-weight: 700;
    font-size: 15px;
    color: var(--ink-dark);
  }
  .rep-block {
    position: absolute;
    left: 660px;
    top: 122px;
    width: 500px;
  }
  .rep-name {
    font-family: "Oswald", "Gill Sans", sans-serif;
    font-weight: 400;
    font-size: 52px;
    line-height: 1;
    letter-spacing: 2px;
    color: var(--brand-pink);
    white-space: nowrap;
  }
  .rep-contacts {
    list-style: none;
    margin-top: 22px;
  }
  .contact-line {
    display: flex;
    align-items: center;
    gap: 20px;
    height: 54px;
    font-family: "Cabin", "Gill Sans", sans-serif;
    font-weight: 500;
    font-size: 27px;
    letter-spacing: 1px;
    color: var(--ink-dark);
  }
  .contact-icon {
    width: 30px;
    height: 30px;
    flex: none;
  }
  .service-line {
    position: absolute;
    right: 60px;
    bottom: 44px;
    font-family: "Cabin", "Gill Sans", sans-serif;
    font-weight: 600;
    font-size: 24px;
    letter-spacing: 1px;
    color: var(--ink-light);
  }
</style>
</head>
<body>
<main class="business-card">
  <svg class="card-shapes" viewBox="0 0 1200 700" aria-hidden="true">
    <defs>
      <linearGradient id="wave-main" x1="0" y1="0" x2="0" y2="1">
        <stop offset="0" stop-color="var(--wave-pink)"/>
        <stop offset="0.45" stop-color="#ee50e0"/>
        <stop offset="1" stop-color="var(--wave-fade)"/>
      </linearGradient>
    </defs>
    <path class="sweep-light" d="M0 180 C 200 330, 650 360, 1200 200 L 1200 230 C 650 380, 200 360, 0 230 Z" fill="#f6f7f7" opacity="0.8"/>
    <path class="wave-back" d="M0 478 C 120 440, 220 425, 330 440 C 600 470, 900 540, 1200 572 L 1200 700 L 0 700 Z" fill="var(--wave-soft)" opacity="0.75"/>
    <path class="wave-front" d="M0 526 C 110 480, 220 462, 360 475 C 650 500, 950 560, 1110 566 C 1150 567, 1180 560, 1200 552 L 1200 700 L 0 700 Z" fill="url(#wave-main)"/>
  </svg>

  <header class="brand-block">
    <div class="brand-name"><span class="brand-dot"></span>Kelvra</div>
    <div class="brand-website">www.gokelvara.example</div>
  </header>

  <section class="rep-block">
    <h1 class="rep-name">REPRESENTATIVE NAME</h1>
    <ul class="rep-contacts">
      <li class="contact-line">
        <svg class="contact-icon" viewBox="0 0 30 30" aria-label="Phone">
          <rect x="8" y="4" width="14" height="24" rx="1.5" fill="var(--ink-dark)"/>
          <rect x="18" y="0" width="2" height="5" fill="var(--ink-dark)"/>
          <rect x="10" y="7" width="10" height="8" fill="#fff"/>
          <g fill="#fff">
            <rect x="10" y="17" width="2.4" height="2"/><rect x="13.8" y="17" width="2.4" height="2"/><rect x="17.6" y="17" width="2.4" height="2"/>
            <rect x="10" y="21" width="2.4" height="2"/><rect x="13.8" y="21" width="2.4" height="2"/><rect x="17.6" y="21" width="2.4" height="2"/>
          </g>
        </svg>
        <span>123-456-7890</span>
      </li>
      <li class="contact-line">
        <svg class="contact-icon" viewBox="0 0 30 30" aria-label="Email">
          <rect x="1" y="6" width="28" height="18" fill="var(--ink-dark)"/>
          <path d="M3 8 L15 17 L27 8" fill="none" stroke="#fff" stroke-width="1.6"/>
          <path d="M3 22 L11 14 M27 22 L19 14" stroke="#fff" stroke-width="1.4"/>
        </svg>
        <span>sampleid@sample.com</span>
      </li>
    </ul>
  </section>

  <p class="service-line">Customer Service 1-800-482-Kelvra</p>
</main>
</body>
</html>
```